Buchcover-Design für Drama/Thriller/Krimi
Zielgruppe
Wir sind eine Publikation und suchen aktuell eine Design für ein Cover eines Drama-Thriller-Krimi Buches.
Zielgruppe sind alle Menschen ab 18 Jahren.
Aufgabenstellung
Es sollte zu einem Drama-Thriller-Krimi passen. Das Buch beinhaltet knapp 280 Seiten und es endet mit einem Selbstmord am Strand.
Das Buch wird heißen: kuşlar yağmurda. Es ist türkisch und heißt 'die Vögel sind im kalten Regen'.
Es handelt über folgendes: Ein Kind wird entführt - es wird die Organ Mafia beschuldigt am Ende stellt sich heraus das der neue Partner der Mutter das Kind entführt hat. Die Mutter wusste Bescheid. Die Geschichte wird von der Sicht eines Journalisten erzählt. Der Mann der Selbstmord begeht ist der Journalist.
Der Autor ist Kemal Duruöz und soll auch auf dem Cover sein. Hinten auf der Rückseite soll ein Platz für einen Kurztext gelassen werden.
Buchformat ist : 13,5×19,5 cm Hochformat.
Das Design des Covers soll die Trauer wiedergeben.
Tipp: Zb. könnte es ein Mann am Strand alleine widerspiegeln. Wir sind aber offen auch für andere Vorschläge.

```html
<!DOCTYPE html>
<html lang="tr">
<head>
<meta charset="utf-8">
<title>kuşlar yağmurda – Kemal Duruöz</title>
<link rel="stylesheet" href="https://fonts.googleapis.com/css2?family=Roboto+Condensed:wght@400&family=Rubik+Distressed&display=swap">
<style>
  :root {
    --cover-red: #cc1719;
    --band-text: #ffffff;
    --title-shadow: #1a1a1a;
    --photo-white: #fafafa;
    --photo-light: #d4d4d4;
    --photo-mid: #a6a6a6;
    --photo-dark: #2b2b2b;
    --photo-black: #0d0d0d;
  }
  html, body {
    margin: 0;
    padding: 0;
    overflow: hidden;
    background: #ffffff;
  }
  .cover {
    position: relative;
    width: 831px;
    height: 1200px;
    overflow: hidden;
    background: var(--photo-light);
  }
  .cover-photo {
    position: absolute;
    inset: 0;
    background:
      linear-gradient(180deg, #ffffff 0%, var(--photo-white) 7%, rgba(250,250,250,0.6) 12%, rgba(250,250,250,0) 19%),
      radial-gradient(ellipse 120px 220px at 110px 470px, rgba(60,60,60,0.75) 0%, rgba(60,60,60,0) 100%),
      radial-gradient(ellipse 260px 140px at 300px 1010px, rgba(13,13,13,0.85) 0%, rgba(13,13,13,0) 100%),
      linear-gradient(155deg, rgba(0,0,0,0) 58%, rgba(20,20,20,0.75) 72%, rgba(40,40,40,0.55) 85%, rgba(150,150,150,0.3) 100%),
      linear-gradient(180deg, var(--photo-mid) 18%, #c2c2c2 45%, #b8b8b8 62%, #e6e6e6 75%, #9a9a9a 100%);
  }
  .band {
    position: absolute;
    left: 136px;
    width: 555px;
    background: var(--cover-red);
    color: var(--band-text);
    font-family: "Roboto Condensed", "Arial Narrow", sans-serif;
    font-weight: 400;
    display: flex;
    align-items: center;
    justify-content: center;
    text-transform: uppercase;
    line-height: 1;
  }
  .band--author {
    top: 0;
    height: 89px;
    font-size: 60px;
    letter-spacing: 6px;
  }
  .band--genre {
    top: 1115px;
    height: 85px;
    font-size: 60px;
    letter-spacing: 7px;
  }
  .title {
    position: absolute;
    left: 0;
    top: 0;
    width: 831px;
    height: 1200px;
  }
  .title text {
    font-family: "Rubik Distressed", sans-serif;
    fill: var(--cover-red);
    filter: url(#title-glow);
  }
</style>
</head>
<body>
<div class="cover">
  <div class="cover-photo" role="img" aria-label="Schwarzweißfoto: eine einsame Gestalt am Strand, im Vordergrund Sand und dunkles Strandgras"></div>

  <div class="band band--author">Kemal Duruöz</div>

  <svg class="title" viewBox="0 0 831 1200" aria-label="kuşlar yağmurda">
    <defs>
      <filter id="title-glow" x="-10%" y="-10%" width="120%" height="120%">
        <feMorphology in="SourceAlpha" operator="dilate" radius="3" result="thick"/>
        <feGaussianBlur in="thick" stdDeviation="4" result="blur"/>
        <feFlood flood-color="#1a1a1a"/>
        <feComposite in2="blur" operator="in" result="shadow"/>
        <feMerge>
          <feMergeNode in="shadow"/>
          <feMergeNode in="SourceGraphic"/>
        </feMerge>
      </filter>
    </defs>
    <text x="296" y="481" font-size="290" textLength="350" lengthAdjust="spacingAndGlyphs">kuşlar</text>
    <text x="39" y="742" font-size="290" textLength="763" lengthAdjust="spacingAndGlyphs">yağmurda</text>
  </svg>

  <div class="band band--genre">Roman</div>
</div>
</body>
</html>
```